Surviving Domestic Violence Flyer

I need a flyer that "POPS" to attract participants for my research project. I have added the important information on my draft flyer.

```html
<!DOCTYPE html>
<html lang="en">
<head>
<meta charset="utf-8">
<title>Survivor Resources Study Flyer</title>
<link rel="stylesheet" href="https://fonts.googleapis.com/css2?family=Anton&family=Oswald:wght@400;500;600;700&family=Open+Sans:wght@400;600;700&display=swap">
<style>
  :root{
    --page:#ffffff;
    --magenta:#c4164c;
    --pink-light:#f07a98;
    --navy:#1f2a8c;
    --maroon:#7a0a2c;
    --yellow:#f7d21e;
    --orange:#f6b21b;
    --white:#ffffff;
    --ink:#2a1a10;
    --text-soft:#fde3ea;
  }
  *{margin:0;padding:0;box-sizing:border-box;}
  html,body{width:1200px;height:1200px;overflow:hidden;background:var(--page);}
  .flyer{
    position:absolute;left:156px;top:26px;width:884px;height:1148px;
    background:linear-gradient(90deg,var(--magenta) 0%,var(--magenta) 58%,#d8346a 75%,var(--pink-light) 100%);
    overflow:hidden;font-family:"Open Sans",Arial,sans-serif;color:var(--white);
  }
  .plate-photo{
    position:absolute;left:600px;top:-10px;width:500px;height:560px;border-radius:50%;
    background:radial-gradient(circle at 45% 50%,#fff7e6 0%,#fbe9ea 30%,#f6c7d3 55%,#ee8fab 75%,rgba(230,90,130,0) 100%);
  }
  .kicker{position:absolute;left:50px;top:52px;font-size:20px;font-weight:600;}
  .study-title{
    position:absolute;left:50px;top:78px;font-family:"Oswald",Arial,sans-serif;font-weight:500;
    font-size:25px;line-height:30px;letter-spacing:0.5px;text-transform:uppercase;
  }
  .headline{
    position:absolute;left:50px;top:186px;font-family:"Anton",Impact,sans-serif;font-size:55px;
    line-height:65px;letter-spacing:7px;text-transform:uppercase;color:#fbf6f6;
    text-shadow:2px 3px 3px rgba(90,0,30,0.45);
  }
  .criteria{position:absolute;left:50px;top:503px;list-style:none;}
  .criteria li{
    display:flex;align-items:center;height:32.8px;font-family:"Oswald",Arial,sans-serif;font-weight:600;
    font-size:23px;letter-spacing:0.6px;color:var(--navy);text-transform:uppercase;
  }
  .criteria svg{width:22px;height:20px;margin-right:7px;flex:none;}
  .details{position:absolute;left:110px;top:738px;width:665px;font-size:14px;line-height:18.5px;color:var(--text-soft);}
  .details p{margin-bottom:18px;}
  .details .hl{color:var(--orange);}
  .details .note{color:var(--navy);}
  .credits{position:absolute;left:110px;top:852px;font-size:14px;line-height:19px;color:var(--text-soft);}
  .credits b{color:var(--maroon);font-weight:700;}
  .egg-icon{
    position:absolute;left:16px;top:832px;width:84px;height:84px;border-radius:14px;
    background:radial-gradient(circle at 50% 50%,#fbe6b8 0%,#ffffff 70%);
  }
  .tabs{position:absolute;left:0;bottom:0;width:884px;height:212px;display:flex;}
  .tab{flex:0 0 44.2px;overflow:hidden;display:flex;border-left:1px dashed rgba(255,255,255,0.5);padding-top:28px;position:relative;}
  .tab::before{content:"";position:absolute;top:9px;left:25px;width:12px;height:12px;border-radius:50%;background:var(--white);box-shadow:inset 0 0 0 3px var(--white),inset 0 0 0 6px var(--orange);}
  .tab span{
    writing-mode:vertical-rl;transform:rotate(180deg);font-weight:600;
    font-size:12.5px;white-space:nowrap;text-align:right;
  }
  .tab .tab-name{background:var(--yellow);color:var(--ink);width:23px;padding-bottom:6px;}
  .tab .tab-phone{color:var(--yellow);width:21px;padding-bottom:6px;}
</style>
</head>
<body>
<main class="flyer">
  <div class="plate-photo" role="img" aria-label="Photo of a cracked egg lying on a white plate"></div>

  <p class="kicker">Request for&nbsp; Study Participants</p>
  <h2 class="study-title">Efficiency of resources available to<br>Suvivors of intimate partner abuse</h2>

  <h1 class="headline">Perceived<br>effectiveness of<br>domestic violence<br>services</h1>

  <ul class="criteria">
    <li><svg viewBox="0 0 22 20"><path d="M11 1 L21 19 H1 Z" fill="var(--orange)"/><rect x="10" y="6.5" width="2" height="7" fill="#fff"/><rect x="10" y="15" width="2" height="2" fill="#fff"/></svg>Are you eighteen years of age or older?</li>
    <li><svg viewBox="0 0 22 20"><path d="M11 1 L21 19 H1 Z" fill="var(--orange)"/><rect x="10" y="6.5" width="2" height="7" fill="#fff"/><rect x="10" y="15" width="2" height="2" fill="#fff"/></svg>Have you been a victim of domestic violence?</li>
    <li><svg viewBox="0 0 22 20"><path d="M11 1 L21 19 H1 Z" fill="var(--orange)"/><rect x="10" y="6.5" width="2" height="7" fill="#fff"/><rect x="10" y="15" width="2" height="2" fill="#fff"/></svg>Have you sought assistance with abuse in the last 12 months?</li>
    <li><svg viewBox="0 0 22 20"><path d="M11 1 L21 19 H1 Z" fill="var(--orange)"/><rect x="10" y="6.5" width="2" height="7" fill="#fff"/><rect x="10" y="15" width="2" height="2" fill="#fff"/></svg>Are you still in contact with the person who abused you?</li>
    <li><svg viewBox="0 0 22 20"><path d="M11 1 L21 19 H1 Z" fill="var(--orange)"/><rect x="10" y="6.5" width="2" height="7" fill="#fff"/><rect x="10" y="15" width="2" height="2" fill="#fff"/></svg>Are you willing and open to discussing your experience with</li>
    <li><svg viewBox="0 0 22 20"><path d="M11 1 L21 19 H1 Z" fill="var(--orange)"/><rect x="10" y="6.5" width="2" height="7" fill="#fff"/><rect x="10" y="15" width="2" height="2" fill="#fff"/></svg>Abuse and your attempts to access services or resources?</li>
  </ul>

  <div class="details">
    <p>If you answered yes to all of these questions, you may be eligible t participate in a study to better understand the resources needed and services expected for survivors of domestic violence.</p>
    <p>Plese contact Dana Mercer at <span class="hl">1(555)014-2290</span> or via e-mail <span class="hl">survivorstudy@example.com</span><br>for additional information. <span class="note">Participants will be compensated for their time.</span></p>
  </div>

  <div class="egg-icon" role="img" aria-label="Small illustration of a fried egg"></div>

  <div class="credits">
    <b>Principal Investigator:</b> Dana Mercer<br>
    <b>Institutional Addiliation:</b> Lakeshore State University, Dept. of Criminology,Law, and Justice<br>
    <b>Contact Address:</b> Post Office Box 10482, Lakeview, IL 60000
  </div>

  <div class="tabs">
    <div class="tab"><span class="tab-name">Survivor Resources Study</span><span class="tab-phone">1(555)014-2290</span></div>
    <div class="tab"><span class="tab-name">Survivor Resources Study</span><span class="tab-phone">1(555)014-2290</span></div>
    <div class="tab"><span class="tab-name">Survivor Resources Study</span><span class="tab-phone">1(555)014-2290</span></div>
    <div class="tab"><span class="tab-name">Survivor Resources Study</span><span class="tab-phone">1(555)014-2290</span></div>
    <div class="tab"><span class="tab-name">Survivor Resources Study</span><span class="tab-phone">1(555)014-2290</span></div>
    <div class="tab"><span class="tab-name">Survivor Resources Study</span><span class="tab-phone">1(555)014-2290</span></div>
    <div class="tab"><span class="tab-name">Survivor Resources Study</span><span class="tab-phone">1(555)014-2290</span></div>
    <div class="tab"><span class="tab-name">Survivor Resources Study</span><span class="tab-phone">1(555)014-2290</span></div>
    <div class="tab"><span class="tab-name">Survivor Resources Study</span><span class="tab-phone">1(555)014-2290</span></div>
    <div class="tab"><span class="tab-name">Survivor Resources Study</span><span class="tab-phone">1(555)014-2290</span></div>
    <div class="tab"><span class="tab-name">Survivor Resources Study</span><span class="tab-phone">1(555)014-2290</span></div>
    <div class="tab"><span class="tab-name">Survivor Resources Study</span><span class="tab-phone">1(555)014-2290</span></div>
    <div class="tab"><span class="tab-name">Survivor Resources Study</span><span class="tab-phone">1(555)014-2290</span></div>
    <div class="tab"><span class="tab-name">Survivor Resources Study</span><span class="tab-phone">1(555)014-2290</span></div>
    <div class="tab"><span class="tab-name">Survivor Resources Study</span><span class="tab-phone">1(555)014-2290</span></div>
    <div class="tab"><span class="tab-name">Survivor Resources Study</span><span class="tab-phone">1(555)014-2290</span></div>
    <div class="tab"><span class="tab-name">Survivor Resources Study</span><span class="tab-phone">1(555)014-2290</span></div>
    <div class="tab"><span class="tab-name">Survivor Resources Study</span><span class="tab-phone">1(555)014-2290</span></div>
    <div class="tab"><span class="tab-name">Survivor Resources Study</span><span class="tab-phone">1(555)014-2290</span></div>
    <div class="tab"><span class="tab-name">Survivor Resources Study</span><span class="tab-phone">1(555)014-2290</span></div>
  </div>
</main>
</body>
</html>
```